Furrow Nova: Supplements for Dogs and Cats needs a Website

1. We need a website to sell our brand of supplements for dogs and cats in the form of chewable treats with delicious flavors. We have Probiotics, calming, hemp, and Hip & Joint formulas. We will have 8 products in total; four for dogs and four for cats. 2. We will need a desktop website as well as a mobile version. We would really like it to look unique, like it was made by a professional; not something pieced together from Plonk. 3. This is meant to be a web store, so we'll need a shopping cart. We would also like to offer rewards, coupons, referral codes, subscription services, an option for customers to donate to a charity (such as the NLBW), and the option for customers to opt in/out of a newsletter. 4. Additionally, we'll need the website to have language options; mainly in English, but including at least Spanish, Italian, and Portuguese. 5. The message we want to convey is sincerity when it comes to the health and welfare of animals; and that we hope to do so in part with our unique formulas, designed by a world-renowned nutritionist, and produced in an FDA approved facility. 6. What we want to see on the site: a. Our slogan: "Healthy is Happy" b. Pages: Home, About, Products, Account, Reviews, Contact Us, FAQ c. Shopping cart d. Social media links: Chatterbox, Chirpline, ClipVault, Snapmosaic e. Shipment tracking

Target Market(s)

Middle age, young adult, elderly.

Industry/Entity Type

Pet Care

Coding

Coded - Design and coding required

Number of Pages Required

5+ page

Colors
fece3e
ec1f27
0355a3
9bcb3c
ffffff

Requirements
Must have
• Logo; slogan (Healthy is Happy); buttons for home, about, products, account, reviews, contact us, FAQ.
• Pictures of dogs and cats (preferably facing the camera).
Nice to have
• We like the look of border collies and golden retrievers. Corgis are nice too, and you can throw in a tiny dog or two.
Should not have
• Bowls of pet food. We make pet treats, not pet food. We don't want to give the wrong impression.

```html
<!DOCTYPE html>
<html lang="en">
<head>
<meta charset="utf-8">
<title>Furrow Nova — Supplements for Dogs and Cats</title>
<link rel="stylesheet" href="https://fonts.googleapis.com/css2?family=Montserrat:wght@400;500;600;700&family=Raleway:ital,wght@0,400;0,500;0,600;0,700;1,400&display=swap">
<style>
:root{
  --teal:#2a9fbc;
  --teal-dark:#1b7f98;
  --orange:#f05a28;
  --orange-dark:#c6431a;
  --amber:#f6a531;
  --brown:#4b1f1e;
  --brown-line:#6a3a37;
  --ink:#2b2b2b;
  --muted:#6d6d6d;
  --white:#ffffff;
}
*{box-sizing:border-box;margin:0;padding:0}
html,body{width:1200px;height:3114px;overflow:hidden}
body{position:relative;background:var(--white);font-family:"Montserrat",sans-serif;color:var(--ink)}
.abs{position:absolute}
a{color:inherit;text-decoration:none}

/* ribbon button */
.ribbon{position:absolute;display:flex;align-items:center;justify-content:center;background:var(--teal);color:var(--white);font:600 12px "Montserrat",sans-serif;height:26px;border-bottom:3px solid var(--teal-dark)}
.ribbon::after{content:"";position:absolute;left:6px;right:6px;bottom:-8px;border-bottom:2px solid var(--teal)}
.ribbon.hot{background:var(--orange);border-bottom-color:var(--orange-dark)}
.ribbon.hot::after{border-bottom-color:var(--orange)}

/* hero */
.hero-photo{position:absolute;left:0;top:0;width:1200px;height:670px;
  background:
    radial-gradient(ellipse 190px 300px at 800px 300px,#9a5530 0%,#a8673f 40%,rgba(190,150,120,.55) 70%,rgba(220,220,225,0) 100%),
    radial-gradient(ellipse 700px 220px at 600px 560px,#ffffff 0%,#f4f4f6 50%,rgba(255,255,255,0) 100%),
    linear-gradient(180deg,#d9dfe6 0%,#eceef1 35%,#cfcfd4 62%,#e6e4e6 80%,#ffffff 100%)}
.topbar-line{position:absolute;top:58px;height:1px;background:#c9cdd3}
.lang{left:87px;top:17px;width:112px;height:25px;border:1px solid #b9bec5;border-radius:13px;font-size:11px;padding:5px 12px;color:#555}
.lang::after{content:"";position:absolute;right:12px;top:10px;border:4px solid transparent;border-top-color:#666}
.mini-social{top:23px;display:flex;gap:16px;left:224px}
.mini-social span{width:11px;height:11px;border-radius:50%;background:#4a4a4a}
.util{top:17px;font-size:11px;color:#555;display:flex;align-items:center;gap:6px;height:25px}
.pill{border:1px solid #b9bec5;border-radius:13px;height:25px;padding:0 12px;display:flex;align-items:center}
.nav{top:74px;font:600 12px "Montserrat",sans-serif;display:flex;gap:28px;color:#222}
.nav .sep{color:#777;font-weight:400}
.nav .on{color:var(--orange);border-bottom:1px solid var(--orange)}
.brand{display:flex;align-items:center;gap:8px;font:700 20px "Montserrat",sans-serif;color:var(--brown);letter-spacing:.5px}
.brand i{width:26px;height:26px;border-radius:50%;background:var(--orange);display:block}
.hero-copy{left:87px;top:250px;width:380px;font:400 29px/35px "Raleway",sans-serif;color:#1d1d1d}
.hero-copy b{font-weight:700}
.dots{left:1098px;top:284px;display:flex;flex-direction:column;gap:15px}
.dots span{width:12px;height:12px;border-radius:50%;border:1px solid #777}
.dots .on{background:radial-gradient(circle,#555 30%,transparent 35%)}

/* about */
.about{position:absolute;left:0;top:664px;width:1200px;height:498px;background:linear-gradient(180deg,#ffffff 0%,#eef1f9 100%)}
.section-title{font:700 29px "Raleway",sans-serif;color:var(--teal)}
.copy{font:400 12px/19px "Montserrat",sans-serif;color:var(--muted)}

/* products */
.featured-title{left:87px;top:1234px;font:400 27px "Raleway",sans-serif;color:#222}
.featured-title b{font-weight:700}
.tabs{top:1244px;left:737px;display:flex;gap:28px;font:600 12px "Montserrat",sans-serif}
.tabs .on{color:var(--orange);border-bottom:1px solid var(--orange)}
.tabs .sep{color:#777;font-weight:400}
.card{position:absolute;top:1302px;width:233px;height:348px;border:2px solid #ececec;background:var(--white)}
.card .shot{position:absolute;left:16px;top:14px;width:199px;height:198px}
.shot.box{background:radial-gradient(ellipse 72px 56px at 50% 50%,#2f56a8 0%,#3c66b8 55%,#d8dde8 85%,#f0f0f0 100%)}
.shot.bag{background:radial-gradient(ellipse 44px 80px at 50% 52%,#ddd6a6 0%,#cfc58f 55%,#e9e7dc 85%,#f0f0f0 100%)}
.card p{position:absolute;left:22px;right:22px;top:236px;text-align:center;font:400 13px/19px "Montserrat",sans-serif;color:#333}
.card .price{position:absolute;left:0;right:0;top:284px;text-align:center;font:600 16px "Montserrat",sans-serif;color:var(--orange)}
.card .ribbon{left:54px;width:125px;top:326px}
.pager{top:1700px;left:568px;display:flex;gap:8px}
.pager span{width:26px;height:26px;border:1px solid #bbb;border-radius:50%;display:flex;align-items:center;justify-content:center;font-size:12px;color:#555}

/* promo */
.promo-photo{left:760px;top:1781px;width:440px;height:384px;
  background:radial-gradient(ellipse 230px 190px at 52% 48%,#d9bb95 0%,#c8a57f 35%,#a8998c 60%,rgba(246,165,49,0) 100%)}
.promo-title{left:87px;top:1876px;font:700 50px "Montserrat",sans-serif;color:var(--teal)}
.promo-sub{left:90px;top:1936px;font:700 36px "Montserrat",sans-serif;color:#262626}
.promo-note{left:90px;top:1997px;font:400 14px "Montserrat",sans-serif;color:#333}

/* testimonials */
.say{left:0;width:1200px;top:2238px;text-align:center;font:400 29px "Raleway",sans-serif;color:#222}
.say b{font-weight:700}
.quote-badge{left:549px;top:2316px;width:102px;height:102px;border-radius:50%;background:var(--brown);display:flex;align-items:center;justify-content:center;color:var(--white);font:700 52px "Raleway",sans-serif;padding-top:22px}
.quote{left:230px;width:740px;top:2438px;text-align:center;font:italic 400 16px/25px "Raleway",sans-serif;color:#555}
.arrow{top:2466px;font:700 24px "Montserrat",sans-serif;color:#222}
.stars{left:0;width:1200px;top:2524px;text-align:center;color:var(--amber);font-size:16px;letter-spacing:2px}
.who{left:0;width:1200px;top:2566px;text-align:center;font:600 12px "Montserrat",sans-serif;color:#222}
.who small{display:block;font-weight:400;color:#666;font-size:11px;margin-top:4px}

/* footer */
.footer{position:absolute;left:0;top:2678px;width:1200px;height:436px;background:var(--brown);color:#e9dcda}
.f-title{font:700 14px "Montserrat",sans-serif;color:var(--white)}
.f-links{list-style:none;font:400 12px/24px "Montserrat",sans-serif}
.f-links .on{color:var(--orange);text-decoration:underline}
.f-contact{font:400 13px/20px "Montserrat",sans-serif}
.f-contact strong{color:var(--white);font-weight:600}
.email-box{left:880px;top:120px;width:230px;height:30px;background:#7a4b48;font:400 11px "Montserrat",sans-serif;color:#d6c3c1;padding:8px 10px}
.email-box::after{content:"";position:absolute;right:10px;top:10px;border:5px solid transparent;border-left:9px solid var(--orange)}
.f-social{left:880px;top:198px;display:flex;gap:15px}
.f-social span{width:26px;height:26px;border-radius:50%;border:1px solid var(--orange)}
.f-social .on{background:var(--orange)}
.f-rule{left:87px;top:336px;width:1023px;height:1px;background:var(--brown-line)}
.f-bottom{top:380px;font:400 11px "Montserrat",sans-serif;color:#e9dcda;display:flex;align-items:center;gap:18px;left:255px}
.f-bar{width:1px;height:12px;background:#b99;display:inline-block}
.foot-brand{left:87px;top:372px;display:flex;align-items:center;gap:8px;font:700 16px "Montserrat",sans-serif;color:var(--white)}
.foot-brand i{width:22px;height:22px;border-radius:50%;background:var(--orange);display:block}
.to-top{left:1094px;top:380px;width:0;height:0;border-left:9px solid transparent;border-right:9px solid transparent;border-bottom:18px solid var(--orange)}
</style>
</head>
<body>

<header>
  <div class="hero-photo" role="img" aria-label="Photo of a red-brown hound dog standing in a frosty winter meadow, fading into white mist at the bottom"></div>

  <div class="abs topbar-line" style="left:87px;width:380px"></div>
  <div class="abs topbar-line" style="left:740px;width:370px"></div>

  <div class="abs lang">English</div>
  <div class="abs mini-social" aria-label="Social links">
    <span title="Chatterbox"></span><span title="Chirpline"></span><span title="ClipVault"></span><span title="Snapmosaic"></span>
  </div>

  <div class="abs util" style="left:858px">
    <svg width="10" height="12" viewBox="0 0 10 12"><path d="M5 0a4 4 0 0 0-4 4c0 3 4 8 4 8s4-5 4-8a4 4 0 0 0-4-4z" fill="#555"/></svg>
    Track My Order
  </div>
  <div class="abs util" style="left:980px"><span class="pill" style="padding:0 7px">
    <svg width="10" height="11" viewBox="0 0 10 11"><circle cx="5" cy="3" r="2.6" fill="#555"/><path d="M0 11a5 4 0 0 1 10 0z" fill="#555"/></svg></span></div>
  <div class="abs util" style="left:1020px"><span class="pill">
    <svg width="12" height="11" viewBox="0 0 12 11" style="margin-right:5px"><path d="M0 1h2l2 6h6l2-5H3" fill="none" stroke="#555"/><circle cx="5" cy="9.5" r="1" fill="#555"/><circle cx="9" cy="9.5" r="1" fill="#555"/></svg>Cart (0)</span></div>

  <div class="abs brand" style="left:512px;top:36px"><i></i>Furrow Nova</div>

  <nav class="abs nav" style="left:87px">
    <a class="on" href="#">Home</a><span class="sep">/</span><a href="#">About Us</a><span class="sep">/</span><a href="#">Products</a>
  </nav>
  <nav class="abs nav" style="left:793px">
    <a href="#">Reviews</a><span class="sep">/</span><a href="#">FAQ</a><span class="sep">/</span><a href="#">Contact Us</a>
  </nav>

  <h1 class="abs hero-copy">We have <b>probiotics, calming, hemp,</b> and <b>hip &amp; joint</b> formulas.</h1>
  <a class="ribbon" href="#" style="left:87px;top:384px;width:141px">Our Products</a>

  <div class="abs dots"><span></span><span class="on"></span><span></span><span></span></div>
</header>

<section class="about">
  <svg class="abs" style="left:88px;top:24px" width="480" height="400" viewBox="0 0 480 400" role="img" aria-label="Portrait of a smiling black and white border collie rising out of a soft blob frame">
    <defs>
      <linearGradient id="collie" x1="0" y1="0" x2="0" y2="1">
        <stop offset="0" stop-color="#2c2727"/>
        <stop offset=".55" stop-color="#4a4242"/>
        <stop offset=".8" stop-color="#b9adab"/>
        <stop offset="1" stop-color="#cbbfbd"/>
      </linearGradient>
    </defs>
    <path d="M60 186 C20 256 30 356 110 371 C170 382 220 356 300 376 C380 396 470 356 460 276 C450 196 380 166 330 136 C300 118 280 100 270 90 Z" fill="none" stroke="#d6d6e0" stroke-width="2"/>
    <path d="M72 194 C36 260 46 348 116 360 C170 369 220 346 295 364 C370 381 450 346 440 276 C432 206 370 176 330 150 C320 60 290 16 220 12 C150 8 110 40 100 100 C96 130 86 164 72 194Z" fill="url(#collie)"/>
  </svg>

  <h2 class="abs section-title" style="left:637px;top:96px">"Healthy is Happy"</h2>
  <p class="abs copy" style="left:637px;top:152px;width:460px">There are many variations of passages of Lorem Ipsum available, but the majority have suffered alteration in some form, by injected humour, or randomised words which don't look even slightly believable. If you are going to use a passage of Lorem Ipsum, you need to be sure there isn't anything embarrassing hidden in the.</p>
  <p class="abs copy" style="left:637px;top:270px;width:460px">All the Lorem Ipsum generators on the Internet tend to repeat predefined chunks as necessary, making this the first ...</p>
  <a class="ribbon hot" href="#" style="left:637px;top:352px;width:160px">Discover About US</a>
</section>

<section>
  <h2 class="abs featured-title">Featured <b>products</b></h2>
  <div class="abs tabs"><span class="on">All</span><span class="sep">/</span><span>Dog</span><span class="sep">/</span><span>Cat</span></div>
  <a class="ribbon" href="#" style="left:984px;top:1237px;width:126px">View All</a>

  <article class="card" style="left:87px">
    <div class="shot box" role="img" aria-label="Product photo of a boxed Kibbleton pouch multipack"></div>
    <p>Contrary to popular belief, Lorem Ipsum is tax</p>
    <div class="price">$10.00</div>
    <a class="ribbon" href="#">Shop Now!</a>
  </article>
  <article class="card" style="left:353px">
    <div class="shot bag" role="img" aria-label="Product photo of a bag of chewable treats"></div>
    <p>Contrary to popular belief, Lorem Ipsum is tax</p>
    <div class="price">$20.00</div>
    <a class="ribbon hot" href="#">Shop Now!</a>
  </article>
  <article class="card" style="left:617px">
    <div class="shot box" role="img" aria-label="Product photo of a boxed Kibbleton pouch multipack"></div>
    <p>Contrary to popular belief, Lorem Ipsum is tax</p>
    <div class="price">$10.00</div>
    <a class="ribbon" href="#">Shop Now!</a>
  </article>
  <article class="card" style="left:880px">
    <div class="shot bag" role="img" aria-label="Product photo of a bag of chewable treats"></div>
    <p>Contrary to popular belief, Lorem Ipsum is tax</p>
    <div class="price">$10.00</div>
    <a class="ribbon" href="#">Shop Now!</a>
  </article>

  <div class="abs pager"><span>‹</span><span>›</span></div>
</section>

<section>
  <svg class="abs" style="left:0;top:1781px" width="1200" height="384" viewBox="0 0 1200 384">
    <path d="M0 25 H560 C640 25 660 -5 740 0 C800 4 820 40 900 45 L1200 45 V384 H0Z" fill="var(--amber)"/>
  </svg>
  <div class="abs promo-photo" role="img" aria-label="Photo of a tan and white dog lying beside a tabby cat, both facing the camera"></div>
  <div class="abs promo-title">10% Off</div>
  <div class="abs promo-sub">Your First Online Order</div>
  <div class="abs promo-note">Contrary to popular belief, Lorem Ipsum is Code: WELCOME at checkout*</div>
  <a class="ribbon" href="#" style="left:90px;top:2053px;width:126px">Order Now!</a>
</section>

<section>
  <h2 class="abs say">What our <b>customers say</b></h2>
  <div class="abs quote-badge">“</div>
  <div class="abs arrow" style="left:156px">‹</div>
  <p class="abs quote">“There are many variations of passages of Lorem Ipsum available, but the majority have suffered alteration in some form, by injected humour, or randomised words which don't look even slightly believable. If you are going”</p>
  <div class="abs arrow" style="left:1028px">›</div>
  <div class="abs stars">★★★★☆</div>
  <div class="abs who">Standard Chunk<small>Lorem ipsum - Designer</small></div>
</section>

<footer class="footer">
  <svg class="abs" style="left:87px;top:70px" width="200" height="176" viewBox="0 0 200 176" role="img" aria-label="Portrait of a smiling black and white border collie in a blob frame">
    <defs>
      <linearGradient id="collieSmall" x1="0" y1="0" x2="0" y2="1">
        <stop offset="0" stop-color="#2a2424"/>
        <stop offset=".6" stop-color="#4a4040"/>
        <stop offset="1" stop-color="#d9cfcd"/>
      </linearGradient>
    </defs>
    <path d="M20 82 C0 122 10 167 60 170 C100 172 120 157 150 164 C185 172 195 132 180 102 C165 72 130 67 110 52" fill="none" stroke="#c8b3b0" stroke-width="1.5"/>
    <path d="M26 86 C8 122 18 162 62 164 C100 166 120 152 148 158 C180 164 186 130 174 104 C166 88 150 80 142 74 C140 30 120 6 90 6 C60 6 44 30 44 58 C38 68 32 76 26 86Z" fill="url(#collieSmall)"/>
  </svg>

  <div class="abs" style="left:367px;top:87px">
    <h3 class="f-title">Quick Links</h3>
    <ul class="f-links" style="margin-top:14px">
      <li>Home</li><li>About</li><li class="on">Products</li><li>Account</li><li>Reviews</li><li>FAQ</li><li>Contact Us</li>
    </ul>
  </div>

  <div class="abs f-contact" style="left:560px;top:87px;width:300px">
    <h3 class="f-title">Contact Us</h3>
    <p style="margin-top:16px"><strong style="font-size:15px">Call Us: (555) 013-2480</strong></p>
    <p>Email: hello@furrownova.example</p>
    <p style="margin-top:18px"><strong>Address:</strong></p>
    <p>4410 Larkspur Meadow Road, Brookvale,<br>QX 20419</p>
  </div>

  <h3 class="abs f-title" style="left:880px;top:87px">Subscribe Us</h3>
  <div class="abs email-box">Enter Your Email...</div>
  <div class="abs f-social" aria-label="Social links">
    <span title="Chatterbox"></span><span class="on" title="Chirpline"></span><span title="ClipVault"></span><span title="Snapmosaic"></span>
  </div>

  <div class="abs f-rule"></div>
  <div class="abs foot-brand"><i></i>Furrow Nova</div>
  <div class="abs f-bottom">
    <span>© 2019 Furrow Nova. All Right Reserved</span><span class="f-bar"></span>
    <span>Terms and Conditions</span><span class="f-bar"></span>
    <span>Privacy Policy</span>
  </div>
  <a class="ribbon" href="#" style="left:882px;top:372px;width:127px">Donate Now!</a>
  <div class="abs to-top"></div>
</footer>

</body>
</html>
```